Update Wordpress website to be captivating, modern and concise

Help us create a cohesive brand and deliver our marketing messages more concisely. We would like to update our Wordpress website to be clean, modern and captivating. Please see the uploaded file for more information on our company, our current website and how we want to continue the relationship beyond the contest. Thank you and we look forward to receiving your creative ideas!

Update: We no longer need you to complete the development.
Updates

We no longer require you to implement the design in Wordpress. Please provide your best, creative designs. Thanks

Target Market(s)

Our customers are companies who are looking for sleek, sexy, easy to use mobile applications for their sales teams. Our customers range from your small to Zenlow 300.

Industry/Entity Type

Marketing

Font styles to use
Sans Serif

Requirements
Must have
• Clean, contemporary, engaging. Comes across as easy to use and inviting. Use the blue in our logo. We do a lot of work on Quorvel Apps and therefore our standard is the Quorvel UX for our styling and UI.
Should not have
• Clutter and distracting.

```html
<!DOCTYPE html>
<html lang="en">
<head>
<meta charset="utf-8">
<title>Brookfen Analytics — Home</title>
<link rel="stylesheet" href="https://fonts.googleapis.com/css2?family=Roboto:wght@400;700&family=Source+Sans+3:wght@400;500&display=swap">
<style>
  :root {
    --sky-dark: #0c161b;
    --sky-mid: #4d5f68;
    --sky-light: #a9b7bd;
    --steel: #2a3136;
    --footer: #07090b;
    --nav-bar: #3a4247;
    --nav-line: #1c2226;
    --text: #ffffff;
    --nav-text: #e6e9eb;
    --brand-blue: #3aa0e6;
    --icon: #f2f2f2;
  }
  * { margin: 0; padding: 0; box-sizing: border-box; }
  html, body { width: 1200px; height: 687px; overflow: hidden; background: var(--footer); }
  .page { position: relative; width: 1200px; height: 687px; overflow: hidden; }

  .hero-photo {
    position: absolute; left: 0; top: 0; width: 1200px; height: 574px;
    background:
      radial-gradient(ellipse 260px 300px at 960px 420px, rgba(30,36,40,.85), rgba(30,36,40,0) 70%),
      radial-gradient(ellipse 420px 260px at 230px 380px, rgba(190,202,207,.55), rgba(190,202,207,0) 70%),
      radial-gradient(ellipse 360px 240px at 560px 480px, rgba(170,183,189,.5), rgba(170,183,189,0) 70%),
      radial-gradient(ellipse 160px 140px at 840px 230px, rgba(200,210,214,.45), rgba(200,210,214,0) 70%),
      linear-gradient(180deg, var(--sky-dark) 0%, #1f3039 22%, var(--sky-mid) 50%, #8797a0 78%, #6f7f87 100%);
  }

  .footer-band {
    position: absolute; left: 0; top: 574px; width: 1200px; height: 113px;
    background: linear-gradient(180deg, #020304 0%, #0b1013 55%, #141b1f 100%);
  }

  .brand {
    position: absolute; left: 206px; top: 20px;
    display: flex; align-items: center; gap: 16px;
  }
  .brand-mark { width: 48px; height: 48px; border-radius: 50%; background: var(--brand-blue); }
  .brand-name {
    font-family: "Roboto", Arial, sans-serif; font-weight: 700; color: var(--text);
    font-size: 36px; line-height: 38px;
  }
  .brand-name span { display: block; }
  .brand-name span + span { padding-left: 20px; }

  .main-nav {
    position: absolute; left: 502px; top: 65px; width: 488px; height: 18px;
    display: flex; background: linear-gradient(180deg, #4a5358, var(--nav-bar) 55%, #2b3236);
    border-radius: 0 4px 4px 0;
  }
  .main-nav a {
    display: flex; align-items: center; justify-content: center;
    font-family: "Source Sans 3", Arial, sans-serif; font-size: 11.5px; letter-spacing: -.2px;
    color: var(--nav-text); text-decoration: none; border-left: 1px solid var(--nav-line);
  }
  .main-nav a:first-child { border-left: none; }
  .main-nav a.is-current { color: var(--brand-blue); }
  .nav-home { width: 52px; } .nav-about { width: 96px; } .nav-team { width: 79px; }
  .nav-management { width: 85px; } .nav-goals { width: 88px; } .nav-contact { width: 88px; }

  .headline {
    position: absolute; left: 207px; top: 190px;
    font-family: "Source Sans 3", Arial, sans-serif; font-weight: 400;
    font-size: 43px; letter-spacing: -2.2px; color: var(--text); white-space: nowrap;
  }

  .intro {
    position: absolute; left: 312px; top: 253px; width: 420px;
    font-family: "Roboto", Arial, sans-serif; font-size: 16.4px; line-height: 16.9px;
    letter-spacing: -.3px; color: var(--text);
  }
  .intro span { display: block; white-space: nowrap; }

  .social {
    position: absolute; left: 911px; top: 627px; display: flex; gap: 2.5px;
  }
  .social span { width: 12px; height: 12px; border-radius: 50%; background: var(--icon); }
</style>
</head>
<body>
<div class="page">
  <div class="hero-photo" role="img" aria-label="Monochrome photo of a steel lattice tower rising into a cloudy sky with soft bokeh light circles"></div>
  <div class="footer-band"></div>

  <header>
    <div class="brand">
      <div class="brand-mark"></div>
      <div class="brand-name"><span>Brookfen</span><span>Analytics</span></div>
    </div>
    <nav class="main-nav">
      <a class="nav-home is-current" href="#">HOME</a>
      <a class="nav-about" href="#">ABOUT US</a>
      <a class="nav-team" href="#">TEAM</a>
      <a class="nav-management" href="#">MANAGEMENT</a>
      <a class="nav-goals" href="#">GOALS</a>
      <a class="nav-contact" href="#">CONTACT US</a>
    </nav>
  </header>

  <main>
    <h1 class="headline">Where mobility meets big data.</h1>
    <p class="intro">
      <span>Are your apps inspiring and insightful? We are a</span>
      <span>boutique company focused on mobile and predictive</span>
      <span>analytics products and solutions. Our software</span>
      <span>products, such as Brookfen Decisions, leverage predictive</span>
      <span>analytics, and a compelling user experience, to assist</span>
      <span>our clients in achieving game changing benefits in their</span>
      <span>marketplace. Our solutions, delivered to our clients,</span>
      <span>include the following: Mobility/ Analytics Strategy and</span>
      <span>Architecture; Mobility Advisory; Big Data Advisory; CoE;</span>
      <span>and Custom Apps. Want to work for Brookfen Analytics?</span>
      <span>Submit your resume.</span>
    </p>
  </main>

  <footer class="social" aria-label="Social links">
    <span></span><span></span><span></span><span></span><span></span><span></span>
  </footer>
</div>
</body>
</html>
```